Boutique Bed and Breakfast needs new website

we require a new website for our 11 room bed and breakfast in the heart of ECHUCA MOAMA. Its an older style establishment and we would love the features on there to take quick fast room bookings. Please check out our current website www.larkholmelodge.com.au We also require it to be Corvix friendly

Target Market(s)

Travellers, corporates accommodation industry

Industry/Entity Type

Accommodation

Number of Pages Required

5+ page

Font styles to use
Sans Serif
Decorative
Script

Colors
86cfc6
33b8a4
00a990
85cae6
ecf7fb
cee9f5
fabb94
f68d4c
f37022

Requirements
Must have
• shopify function or booking button function
Nice to have
• Would like to be able to easily move photos change wording and have a sliding photo's function in the website header

```html
<!DOCTYPE html>
<html lang="en">
<head>
<meta charset="utf-8">
<title>Larkholme Lodge – Home</title>
<link href="https://fonts.googleapis.com/css2?family=Bree+Serif&family=Bungee&family=Merriweather:wght@300;400&display=swap" rel="stylesheet">
<style>
:root{
  --teal:#0b8da7;
  --teal-dark:#0a7e96;
  --sky:#cde9f3;
  --sky-mid:#8fcfdf;
  --ink:#3c3c3c;
  --muted:#6b6b6b;
  --line:#9a9a9a;
  --page:#ffffff;
  --edge:#f4f4f4;
}
*{margin:0;padding:0;box-sizing:border-box}
html,body{width:1200px;height:2250px;overflow:hidden;background:var(--page)}
body{position:relative;font-family:"Merriweather",Georgia,serif;color:var(--ink)}
.abs{position:absolute}
.side-edge{left:1163px;top:0;width:37px;height:2250px;background:var(--edge)}
.header-edge{top:0;height:38px;background:linear-gradient(90deg,#cfe9f2,#e3f3f8)}

/* feature cards */
.feature-card{top:0;height:300px;border:1.5px solid var(--teal);border-top:none;padding:0 22px}
.feature-card h3{font-family:"Bree Serif",Georgia,serif;font-weight:400;color:var(--teal);font-size:23px;margin-top:2px;line-height:34px}
.feature-card p{font-weight:300;font-size:12.5px;line-height:15.5px;color:var(--muted);text-align:justify;hyphens:auto;-webkit-hyphens:auto;margin-top:24px}
.feature-card p + p{margin-top:16px;text-align:left}

/* collage */
.photo{display:block}
.collage-frame{border:6px solid var(--sky)}

/* amenities */
.amenity{width:250px;text-align:center}
.amenity svg{display:block;margin:0 auto}
.amenity h4{font-weight:300;font-size:13px;color:var(--ink);margin-top:14px}
.amenity p{font-weight:300;font-size:7.5px;line-height:9px;color:var(--muted);margin-top:6px;padding:0 6px}

/* section headings */
.display-heading{font-family:"Bungee",Impact,sans-serif;font-weight:400;letter-spacing:2px;line-height:1}
.rooms-heading{left:140px;top:920px;font-size:40px;color:var(--teal);text-shadow:3px 3px 0 var(--sky)}
.reserve-link{left:918px;top:957px;font-size:12.5px;letter-spacing:.5px;color:var(--ink);text-decoration:none}

/* room cards */
.room{top:1014px}
.room-photo{height:189px}
.room h2{font-weight:300;font-size:35px;text-align:center;color:#555;margin-top:20px;line-height:46px}
.room-rule{height:1.5px;background:var(--line);margin-top:14px}
.room-desc{font-weight:300;font-size:9.6px;line-height:12px;text-align:center;color:var(--muted);margin-top:20px;padding:0 38px}
.room-meta{position:relative;height:46px;margin-top:34px}
.room-price{position:absolute;top:0;font-size:18.5px;line-height:22px;color:var(--ink)}
.room-divider{position:absolute;top:0;width:1.5px;height:46px;background:#bdbdbd}
.room-details{position:absolute;top:15px;font-size:13px;color:var(--ink)}

.book-button{left:540px;top:1513px;width:112px;height:30px;background:var(--sky-mid);color:#fff;font-size:10px;letter-spacing:.5px;text-align:center;line-height:30px;text-decoration:none}

/* contact */
.map-area{left:30px;top:1665px;width:921px;height:477px;background:linear-gradient(135deg,#eceff1 0%,#e6ecef 55%,#edf0f2 100%)}
.contact-panel{left:636px;top:1743px;width:426px;height:340px;background:var(--teal);padding:0 48px;color:#fff}
.contact-heading{font-size:40px;color:#fff;margin-top:50px;text-shadow:3px 3px 0 #7cc6dd}
.contact-panel address{font-style:normal;font-weight:300;font-size:16.5px;line-height:21px;margin-top:34px}
.contact-panel p{font-weight:300;font-size:16.5px;line-height:21px}
.footer-band{left:30px;top:2142px;width:1133px;height:55px;background:var(--teal)}
</style>
</head>
<body>

<div class="abs side-edge"></div>
<div class="abs header-edge" style="left:0;width:135px" role="img" aria-label="Edge of the header photo slider"></div>
<div class="abs header-edge" style="left:1050px;width:113px" role="img" aria-label="Edge of the header photo slider"></div>

<!-- Local attractions -->
<section class="abs feature-card" style="left:138px;width:297px">
  <h3>Silver Reed Golf Club</h3>
  <p>Lorem ipsum dolor sit amet, consectetuer adipiscing elit, sed diam Lorem ipsum dolor sit amet, consectetuer adipiscing elit, sed diam Lorem ipsum dolor sit amet, consectetuer adipiscing elit, sed diam Lorem ipsum dolor sit amet, consectetuer adipiscing elit, sed diam Lorem ipsum dolor sit amet, consectetuer adipiscing elit, sed diam Lorem ipsum dolor sit amet, consectetuer adipiscing elit, sed diam</p>
</section>
<section class="abs feature-card" style="left:447px;width:297px">
  <h3>P. S. Wanderer</h3>
  <p>Built in Echuca in 1874 the Wanderer PS has had a long and chequered life working on the Murray River as a tow boat and hawking steamer towing laden barges of wheat, flour, wool, copper ore and building materials servicing outback stations and towns along the Murray river. BOOK NOW FOR THE BELLGROVE STATION TO ECHUCA CRUISE 5 MAY - Hurry limited tickets available! - Go to contact page to download flyer</p>
</section>
<section class="abs feature-card" style="left:759px;width:296px">
  <h3>12 on Carrow</h3>
  <p>Our heritage listed tastefully restored, fully self contained miners cottage offering superb accommodation in the Old Port precinct which is still very much a working port and it boasts the biggest fleet of operating paddlesteamers in the world. Visitors can simply walk to the attractions, restaurants and pubs.</p>
  <p>AVAILABLE FOR LONG TERM AND HOLIDAY RENTAL</p>
</section>

<!-- Photo collage -->
<div class="abs photo" style="left:188px;top:425px;width:270px;height:175px;background:linear-gradient(160deg,#e8e2da,#c9bfb3)" role="img" aria-label="Bright guest room with bed and television"></div>
<div class="abs photo" style="left:138px;top:507px;width:368px;height:239px;background:linear-gradient(120deg,#8e8a5a,#d9cdb4 45%,#b5502f 80%)" role="img" aria-label="Sitting room with green sofas and red brick wall"></div>
<div class="abs photo" style="left:255px;top:618px;width:270px;height:177px;background:linear-gradient(150deg,#d8c9b0,#6e3a1e 60%,#3a1a10)" role="img" aria-label="Bedroom with timber table, wine and fruit platter"></div>
<div class="abs collage-frame" style="left:258px;top:483px;width:195px;height:185px"></div>

<!-- Amenities -->
<div class="abs amenity" style="left:580px;top:480px">
  <svg width="44" height="40" viewBox="0 0 44 40" fill="none" stroke="#0b8da7" stroke-width="2"><rect x="3" y="9" width="36" height="27" rx="3"/><path d="M8 9l20-6 3 6"/><rect x="28" y="18" width="13" height="9" rx="2"/><circle cx="33" cy="22.5" r="1.3" fill="#0b8da7"/></svg>
  <h4>Reasonable Prices</h4>
  <p>Fair nightly rates with no hidden fees, seasonal specials and discounts for longer stays all year round.</p>
</div>
<div class="abs amenity" style="left:817px;top:480px">
  <svg width="44" height="40" viewBox="0 0 44 40" fill="none" stroke="#0b8da7" stroke-width="2" stroke-linejoin="round"><path d="M22 36C10 27 4 21 4 13a8.5 8.5 0 0 1 18-4 8.5 8.5 0 0 1 18 4c0 8-6 14-18 23z"/></svg>
  <h4>Family Friendly</h4>
  <p>Spacious rooms, cots on request and easy walks to parks, the river and the historic port precinct.</p>
</div>
<div class="abs amenity" style="left:580px;top:630px">
  <svg width="30" height="40" viewBox="0 0 30 40" fill="none" stroke="#0b8da7" stroke-width="2"><circle cx="15" cy="6" r="2"/><path d="M4 22a11 11 0 0 1 22 0z"/><path d="M2 26h26"/><path d="M6 30h18M9 34h12"/></svg>
  <h4>Full Room Service</h4>
  <p>Breakfast delivered to your door, fresh linen daily and a friendly host ready to help with anything.</p>
</div>
<div class="abs amenity" style="left:817px;top:630px">
  <svg width="44" height="40" viewBox="0 0 44 40" fill="none" stroke="#0b8da7" stroke-width="2"><rect x="4" y="8" width="36" height="28" rx="3"/><path d="M16 8V3h12v5"/><rect x="9" y="13" width="26" height="18" rx="2"/><path d="M15 26l4-6 4 4 4-7"/></svg>
  <h4>Travel accomodation</h4>
  <p>Ideal base for corporate travellers and tourists, with parking, wifi and quick booking confirmation.</p>
</div>

<!-- Rooms -->
<h2 class="abs display-heading rooms-heading">OUR ROOMS</h2>
<a class="abs reserve-link" href="#">MAKE&nbsp; A RESERVATION</a>

<article class="abs room" style="left:138px;width:285px">
  <div class="room-photo" style="background:linear-gradient(140deg,#efe6d6,#b59a7a 45%,#5a2a16)" role="img" aria-label="Room 1 with double bed and wine on table"></div>
  <h2>Room 1</h2>
  <div class="room-rule" style="margin-left:15px;width:247px"></div>
  <p class="room-desc">Lorem ipsum dolor sit amet, consectetuer adipiscing elit, sed diam nonummy nibh euismod tincidunt ut laoreet dolore molore te feugait nulla facilisi. &nbsp;dolor sit amet, consectetuer adipiscing elit, sed diam nonummy nibh euismod tincidunt ut laoreet dolore molore te feugait nulla facilisi.</p>
  <div class="room-meta"><span class="room-price" style="left:42px">From<br>$199</span><span class="room-divider" style="left:120px"></span><span class="room-details" style="left:144px">VIEW DETAILS</span></div>
</article>

<article class="abs room" style="left:449px;width:286px">
  <div class="room-photo" style="background:linear-gradient(150deg,#f1ece6,#c7bcb2 50%,#4a1c18)" role="img" aria-label="Room 2 lounge with television and sofa"></div>
  <h2>Room 2</h2>
  <div class="room-rule" style="margin-left:4px;width:247px"></div>
  <p class="room-desc" style="padding:0 50px 0 26px">Lorem ipsum dolor sit amet, consectetuer adipiscing elit, sed diam nonummy nibh euismod tincidunt ut laoreet dolore molore te feugait nulla facilisi. &nbsp;dolor sit amet, consectetuer adipiscing elit, sed diam nonummy nibh euismod tincidunt ut laoreet dolore molore te feugait nulla facilisi.</p>
  <div class="room-meta"><span class="room-price" style="left:31px">From<br>$199</span><span class="room-divider" style="left:107px"></span><span class="room-details" style="left:131px">VIEW DETAILS</span></div>
</article>

<article class="abs room" style="left:770px;width:292px">
  <div class="room-photo" style="background:linear-gradient(130deg,#efe9df,#b4693f 45%,#7a1820)" role="img" aria-label="Room 3 sitting area with green sofas and brick wall"></div>
  <h2>Room 3</h2>
  <div class="room-rule" style="margin-left:15px;width:247px"></div>
  <p class="room-desc" style="padding:0 44px 0 34px">Lorem ipsum dolor sit amet, consectetuer adipiscing elit, sed diam nonummy nibh euismod tincidunt ut laoreet dolore molore te feugait nulla facilisi. &nbsp;dolor sit amet, consectetuer adipiscing elit, sed diam nonummy nibh euismod tincidunt ut laoreet dolore molore te feugait nulla facilisi.</p>
  <div class="room-meta"><span class="room-price" style="left:41px">From<br>$199</span><span class="room-divider" style="left:118px"></span><span class="room-details" style="left:142px">VIEW DETAILS</span></div>
</article>

<a class="abs book-button" href="#">BOOK ROOMS</a>

<!-- Contact -->
<div class="abs map-area" role="img" aria-label="Street map of Echuca showing the lodge location by the river"></div>
<section class="abs contact-panel">
  <h2 class="display-heading contact-heading">CONTACT US</h2>
  <address>Larkholme Lodge Echuca<br>14 Riverbend Parade, Echuca, 3564</address>
  <p style="margin-top:21px">Tel: (03) 5550 1234</p>
  <p style="margin-top:21px">Fax: (03) 5550 1235</p>
  <p style="margin-top:19px">stay@larkholmelodge.com.au</p>
</section>
<footer class="abs footer-band"></footer>

</body>
</html>
```